Book Cover Design - Uncovering Weight Loss Secrets

I need a book cover design for a book called 'Folding The Map'. It is a book that goes through all of the secrets to weight loss, without any crazy shakes or workouts or pills or potions. The book is really focused on helping people understand that Weight loss is simple and has more to do with our mindset as well as the food we were eating. It is about taking personal responsibility not looking for the next fancy revolutionary product that is going to help them magically melt the fat away. The book is pragmatic in nature and breaks down in simple terms how we can lose weight and keep it off for the rest of our lives. It shows the user that it is simple to lose weight, but it takes effort. They should stop looking for a quick fix when it comes to weight loss but instead eat healthy for the rest of their lives.
The book is intended to be hard-hitting no holds barred approach. The book has the same title as my business name. I will attach the current logo that we use in the business. This doesn't need to be on the front of the book maybe at the back down the bottom somewhere.
I am looking to have both an e-book cover and a standard printed book cover.
I don't have any colours in mind, my logo can be adapted to be different colours or just white.
The message that I am wanting people to feel when they see my book, is that all these Weightloss fads are a joke, that I know the secrets that will get them to their weight loss goal even if they fail at everything else before.
On the cover it should say the following.
FOLDING THE MAP
Uncovering the Weight Loss Secrets
The big companies have been trying to keep hidden for years!
COLIN MAYHEW
People who have failed many times trying to lose weight & need help
Weight Loss

```html
<!DOCTYPE html>
<html lang="en">
<head>
<meta charset="utf-8">
<title>Folding The Map – Book Cover</title>
<link rel="stylesheet" href="https://fonts.googleapis.com/css2?family=Fira+Sans+Condensed:wght@700;800&family=Open+Sans:wght@700&display=swap">
<style>
  :root {
    --backdrop: #cbcbcb;
    --paper: #ffffff;
    --green: #00743a;
    --red: #bc1a14;
    --apple-light: #c8202a;
    --apple-red: #a5121b;
    --apple-dark: #6e0a12;
    --white: #ffffff;
  }
  html, body {
    margin: 0;
    width: 1200px;
    height: 1200px;
    overflow: hidden;
    background: var(--backdrop);
  }
  .cover {
    position: absolute;
    left: 243px;
    top: 62px;
    width: 711px;
    height: 1066px;
    background: var(--paper);
    box-shadow: 8px 10px 18px rgba(0, 0, 0, 0.18);
  }
  .cover svg { display: block; width: 100%; height: 100%; }
  .title { font-family: "Fira Sans Condensed", sans-serif; font-weight: 800; }
  .title--green { fill: var(--green); font-size: 172px; }
  .title--red { fill: var(--red); font-size: 182px; }
  .subtitle { font-family: "Fira Sans Condensed", sans-serif; font-weight: 700; }
  .subtitle--red { fill: var(--red); font-size: 52px; }
  .subtitle--green { fill: var(--green); font-size: 40px; }
  .author-band { fill: var(--red); }
  .author { font-family: "Open Sans", sans-serif; font-weight: 700; font-size: 50px; fill: var(--white); }
</style>
</head>
<body>
  <div class="cover">
    <svg viewBox="0 0 711 1066" xmlns="http://www.w3.org/2000/svg">
      <defs>
        <radialGradient id="apple-tone" cx="42%" cy="38%" r="62%">
          <stop offset="0%" stop-color="var(--apple-light)"/>
          <stop offset="55%" stop-color="var(--apple-red)"/>
          <stop offset="100%" stop-color="var(--apple-dark)"/>
        </radialGradient>
      </defs>

      <ellipse class="cover-photo" cx="357" cy="548" rx="202" ry="196" fill="url(#apple-tone)"
               role="img" aria-label="Photo of a red apple with green leaves, wrapped in a measuring tape"/>

      <text class="title title--green" x="73" y="178" textLength="576" lengthAdjust="spacingAndGlyphs">FOLDING</text>
      <text class="title title--red" x="71" y="325" textLength="578" lengthAdjust="spacingAndGlyphs">THE MAP</text>

      <text class="subtitle subtitle--red" x="216" y="820" textLength="288" lengthAdjust="spacingAndGlyphs">UNCOVERING</text>
      <text class="subtitle subtitle--red" x="84" y="870" textLength="555" lengthAdjust="spacingAndGlyphs">THE WEIGHT LOSS SECRETS</text>
      <text class="subtitle subtitle--green" x="73" y="914" textLength="572" lengthAdjust="spacingAndGlyphs">THE BIG COMPANIES HAVE BEEN TRYING</text>
      <text class="subtitle subtitle--green" x="155" y="952" textLength="410" lengthAdjust="spacingAndGlyphs">TO KEEP HIDDEN FOR YEARS!</text>

      <rect class="author-band" x="0" y="979" width="711" height="87"/>
      <text class="author" x="153" y="1041" textLength="421" lengthAdjust="spacing">COLIN MAYHEW</text>
    </svg>
  </div>
</body>
</html>
```